LH Business Card NEEDED

Lumen Harbour is a finance brokering company that provide lending advise to consumer, business, corporate, and property developer for all their financing needs.

We source and match customer needs in Home Loan, Business Loan, Commercial Property Loan, Assets Finance, and other banking related services. It is a market with full of loans! But we specialise in more complex loan structure and our client base are more business and corporate level. Our suppliers are Banks and large Financial Institution where these business card will go to.

We have a great deal of Asian clients, therefore the card need to also include Chinese language together with English.

Refer to attached file for logo and content requirements.

We are looking for designs with the following ingredients:
* Innovative & Creative
* Professional
* Trust & Security

Please pick colours that will compliment the colours of the company logo.

Please provide a unique design, for example the edge of the card is rounded or corner cut off.
Updates

Company logo uploaded.

Please commence submitting your design.

Target Market(s)

Target audiences are businessmen, corporate, and property developer. And also a great deal of Chinese clients.

Industry/Entity Type

Finance

Contact Information for Business Card

Lumen Harbour Pty. Ltd.
Morris Okafor
Director
Suite 42, 7-9 Pellow St. Dunmore NSW 2738

Requirements
Must have
• Double sided design

```html
<!DOCTYPE html>
<html lang="en">
<head>
<meta charset="utf-8">
<title>Lumen Harbour – Business Card</title>
<link href="https://fonts.googleapis.com/css2?family=Cormorant+SC:wght@500;600&family=Noto+Serif+TC:wght@500&family=Open+Sans:wght@600&display=swap" rel="stylesheet">
<style>
  :root {
    --backdrop: #e4e4e2;
    --navy-light: #23528c;
    --navy-mid: #12305a;
    --navy-dark: #0a1830;
    --silver-hi: #fbfbfb;
    --silver-mid: #d4d5d7;
    --silver-low: #a9abae;
    --ink: #1c1c1e;
    --rule-dark: #8e9094;
    --rule-light: #a8b3c4;
    --pale-text: #d9dee6;
    --white: #ffffff;
    --gold: #c9a245;
  }
  * { box-sizing: border-box; margin: 0; padding: 0; }
  html, body {
    width: 1200px; height: 900px; overflow: hidden;
    background: var(--backdrop);
  }
  .stage { position: relative; width: 1200px; height: 900px; }

  .card {
    position: absolute; left: 290px; width: 620px; height: 379px;
    border-radius: 0 90px 0 90px;
    overflow: hidden;
    box-shadow: 0 10px 28px rgba(0,0,0,.22);
  }

  /* Front side */
  .card--front {
    top: 50px;
    background: radial-gradient(ellipse at 55% 30%, var(--navy-light) 0%, var(--navy-mid) 45%, var(--navy-dark) 100%);
  }
  .front__mark {
    position: absolute; left: 270px; top: 48px; width: 80px; height: 80px;
    border-radius: 50%;
    background: radial-gradient(circle at 40% 35%, var(--silver-hi), var(--silver-low));
    border: 10px solid var(--silver-mid);
    box-shadow: inset 0 0 0 12px var(--gold);
  }
  .front__name {
    position: absolute; left: 0; right: 0; top: 150px; text-align: center;
    font-family: "Cormorant SC", serif; font-weight: 500;
    font-size: 30px; letter-spacing: 14px; color: var(--pale-text);
  }
  .front__rule {
    position: absolute; left: 90px; right: 90px; top: 212px;
    height: 1px; background: var(--rule-light);
  }
  .front__chinese {
    position: absolute; left: 0; right: 0; top: 194px; text-align: center;
    font-family: "Noto Serif TC", serif; font-size: 26px; letter-spacing: 4px;
    color: var(--white);
  }
  .front__chinese span { background: var(--navy-mid); padding: 0 14px; }
  .front__tagline {
    position: absolute; right: 90px; top: 262px;
    font-family: "Open Sans", sans-serif; font-weight: 600;
    font-size: 30px; color: var(--white);
  }

  /* Back side */
  .card--back {
    top: 471px;
    background: linear-gradient(180deg, var(--silver-mid) 0%, var(--silver-hi) 22%, var(--silver-low) 48%, var(--silver-hi) 70%, var(--silver-mid) 100%);
  }
  .back__brand { position: absolute; left: 36px; top: 26px; width: 250px; text-align: center; }
  .back__mark {
    display: block; margin: 0 auto 6px; width: 52px; height: 52px; border-radius: 50%;
    background: radial-gradient(circle at 40% 35%, var(--silver-hi), var(--silver-low));
    border: 7px solid var(--silver-mid);
    box-shadow: inset 0 0 0 8px var(--gold), 0 1px 2px rgba(0,0,0,.25);
  }
  .back__name {
    font-family: "Cormorant SC", serif; font-weight: 600;
    font-size: 17px; letter-spacing: 6px; color: var(--ink);
  }
  .back__chinese {
    font-family: "Noto Serif TC", serif; font-size: 16px; letter-spacing: 2px;
    color: var(--ink); border-bottom: 1px solid var(--rule-dark); padding-bottom: 6px;
  }
  .person { position: absolute; right: 56px; top: 128px; text-align: center; color: var(--ink); }
  .person__name {
    font-family: "Cormorant SC", serif; font-weight: 600; font-size: 34px; letter-spacing: 1px;
  }
  .person__chinese { font-family: "Noto Serif TC", serif; font-size: 26px; line-height: 1.2; }
  .person__title { font-family: "Cormorant SC", serif; font-weight: 600; font-size: 24px; letter-spacing: 1px; }
  .person__title span { font-family: "Noto Serif TC", serif; font-size: 22px; margin-left: 10px; }
  .back__rule {
    position: absolute; left: 0; right: 0; top: 286px; height: 1px; background: var(--rule-dark);
  }
  .contacts {
    position: absolute; left: 60px; right: 80px; top: 306px;
    display: flex; justify-content: space-between;
    font-family: "Cormorant SC", serif; font-weight: 600; font-size: 24px;
    letter-spacing: 1px; color: var(--ink); list-style: none;
  }
</style>
</head>
<body>
<main class="stage">
  <section class="card card--front" aria-label="Card front">
    <span class="front__mark"></span>
    <p class="front__name">Lumen Harbour</p>
    <span class="front__rule"></span>
    <p class="front__chinese"><span>明港通</span></p>
    <p class="front__tagline">make me an offer</p>
  </section>

  <section class="card card--back" aria-label="Card back">
    <div class="back__brand">
      <span class="back__mark"></span>
      <p class="back__name">Lumen Harbour</p>
      <p class="back__chinese">明港通</p>
    </div>
    <div class="person">
      <p class="person__name">Morris Okafor Lam</p>
      <p class="person__chinese">林明遠</p>
      <p class="person__title">Director<span>董事</span></p>
    </div>
    <span class="back__rule"></span>
    <ul class="contacts">
      <li>Mobile</li>
      <li>Email</li>
      <li>Website</li>
    </ul>
  </section>
</main>
</body>
</html>
```